Crime/mystery/thriller novel cover design

I am looking to get a cover designed for a novel. It is a crime/mystery/thriller set in Liverpool, England, between the 1970s and current day. I have permission to use some paintings by an artist for the cover, so it just needs put together and jazzed up. I am looking for something which has a fairly classic feel (so not just pulp airport thriller trash) but with some flair nonetheless.
The novel will be paperback, 127mm x 203mm with approx 18mm spine width. Can be gloss or matt cover, would be interesting to discuss.
The title is:
THE CASTLEMERE TIDE
Author name:
ROBERT J. KELVANSKI
Publisher:
VELUMBRA PUBLISHING LTD (or simply VELUMBRA)

I am still working on the back cover blurb but I will upload this when finished.
There are 4 images I could use for the cover though my favourite is the one called Evening, Harwick Docklands.

```html
<!DOCTYPE html>
<html lang="en">
<head>
<meta charset="utf-8">
<title>The Castlemere Tide — Cover Wrap</title>
<link href="https://fonts.googleapis.com/css2?family=Cinzel:wght@400;500&family=Great+Vibes&family=Allura&family=Barlow+Semi+Condensed:wght@600&display=swap" rel="stylesheet">
<style>
  :root {
    --page-bg: #d9d9db;
    --gold: #ebe27e;
    --gold-soft: #e6dc8a;
    --ink: #111111;
    --paper-white: #f4f1e6;
    --sky-dark: #262d2a;
    --sky-olive: #4c5a3c;
    --glow-yellow: #f0c632;
    --glow-orange: #e58a22;
    --ember: #9c4a1a;
    --water-dark: #2e2418;
  }
  * { margin: 0; padding: 0; box-sizing: border-box; }
  html, body { width: 1200px; height: 900px; overflow: hidden; background: var(--page-bg); }

  .cover-wrap {
    position: absolute; left: 110px; top: 84px;
    width: 979px; height: 731px;
    display: grid; grid-template-columns: 457px 65px 457px;
    box-shadow: 0 10px 30px rgba(0,0,0,0.25);
  }
  .cover-artwork {
    position: absolute; inset: 0;
    background:
      radial-gradient(ellipse 45% 14% at 52% 49%, rgba(255,236,120,0.85), rgba(255,236,120,0) 70%),
      linear-gradient(180deg, var(--sky-dark) 0%, var(--sky-olive) 30%, #a9a23a 42%, var(--glow-yellow) 50%, var(--glow-orange) 60%, var(--ember) 78%, var(--water-dark) 100%);
  }
  .panel { position: relative; }

  /* Back cover */
  .back-cover { padding: 58px 28px 0 44px; }
  .blurb-panel {
    border-radius: 26px;
    background: linear-gradient(180deg, rgba(150,140,70,0.85), rgba(120,120,50,0.55));
    padding: 34px 30px 26px;
    text-align: center;
    color: var(--paper-white);
  }
  .blurb-title .title-small { font-family: "Cinzel", serif; font-size: 15px; color: var(--gold); letter-spacing: 1px; line-height: 1; }
  .blurb-title .title-script { font-family: "Great Vibes", cursive; font-size: 40px; color: var(--gold); line-height: 0.9; }
  .blurb-text {
    font-family: "Allura", cursive; font-size: 18px; line-height: 1.35;
    margin-top: 16px; text-align: center;
  }
  .blurb-author {
    font-family: "Barlow Semi Condensed", sans-serif; font-size: 11px; letter-spacing: 1px;
    margin-top: 14px;
  }

  /* Spine */
  .spine {
    display: flex; flex-direction: column; align-items: center;
    background: linear-gradient(90deg, rgba(0,0,0,0.15), rgba(0,0,0,0) 30%, rgba(0,0,0,0) 70%, rgba(0,0,0,0.15));
  }
  .spine-author {
    writing-mode: vertical-rl; margin-top: 18px;
    font-family: "Barlow Semi Condensed", sans-serif; font-size: 19px; letter-spacing: 1.5px;
    color: var(--ink);
  }
  .spine-title { writing-mode: vertical-rl; margin-top: 36px; display: flex; align-items: center; }
  .spine-title .title-small { font-family: "Cinzel", serif; font-size: 11px; color: var(--ink); line-height: 1; }
  .spine-title .title-script { font-family: "Great Vibes", cursive; font-size: 34px; color: var(--paper-white); line-height: 1; }
  .spine-publisher {
    writing-mode: vertical-rl; margin-top: auto; margin-bottom: 0;
    width: 100%; padding: 12px 0; background: var(--ink);
    display: flex; align-items: center;
    font-family: "Barlow Semi Condensed", sans-serif; font-size: 11px; letter-spacing: 1.5px; color: var(--paper-white);
  }

  /* Front cover */
  .front-title {
    position: absolute; left: 40px; top: 96px;
    color: var(--gold);
  }
  .front-title .title-the { font-family: "Cinzel", serif; font-size: 22px; letter-spacing: 1px; line-height: 1; display: block; }
  .front-title .title-caps { font-family: "Cinzel", serif; font-size: 36px; letter-spacing: 1px; line-height: 1; display: block; }
  .front-title .title-script {
    font-family: "Great Vibes", cursive; font-size: 132px; line-height: 0.8;
    display: block; margin-left: 92px; margin-top: -4px;
  }
  .front-author {
    position: absolute; left: 90px; top: 440px;
    font-family: "Barlow Semi Condensed", sans-serif; font-size: 30px; letter-spacing: 1px;
    color: var(--gold-soft);
    padding-bottom: 4px; border-bottom: 3px solid var(--gold-soft);
  }
  .front-publisher {
    position: absolute; right: 0; bottom: 20px;
    background: var(--ink); color: var(--paper-white);
    font-family: "Barlow Semi Condensed", sans-serif; font-size: 17px; letter-spacing: 1.5px;
    padding: 6px 14px;
  }
</style>
</head>
<body>
  <main class="cover-wrap">
    <div class="cover-artwork" role="img" aria-label="Painting: Evening, Harwick Docklands — silhouetted waterfront skyline against a glowing yellow and orange sunset reflected in the river"></div>

    <section class="panel back-cover">
      <div class="blurb-panel">
        <div class="blurb-title">
          <div class="title-small">THE CASTLEMERE</div>
          <div class="title-script">Tide</div>
        </div>
        <p class="blurb-text">It is a crime/mystery/thriller set in Liverpool, England, between the 1970s and current day. I have permission to use some paintings by an artist for the cover, so it just needs put together and jazzed up. I am looking for something which has a fairly classic feel (so not just pulp airport thriller trash) but with some flair nonetheless.</p>
        <p class="blurb-author">ROBERT J. KELVANSKI</p>
      </div>
    </section>

    <section class="panel spine">
      <div class="spine-author">ROBERT J. KELVANSKI</div>
      <div class="spine-title">
        <span class="title-small">THE CASTLEMERE</span>
        <span class="title-script">Tide</span>
      </div>
      <div class="spine-publisher">VELUMBRA</div>
    </section>

    <section class="panel front-cover">
      <h1 class="front-title">
        <span class="title-the">THE</span>
        <span class="title-caps">CASTLEMERE</span>
        <span class="title-script">Tide</span>
      </h1>
      <p class="front-author">ROBERT J. KELVANSKI</p>
      <p class="front-publisher">VELUMBRA</p>
    </section>
  </main>
</body>
</html>
```